Home page design for Drone video business (the Business focusses on home videos for realtors)

Dear reader,

*I NEED DESIGNS OF ALL THE PAGES*
We need a first design of a homepage and of 4 other pages of the website of a business that sells drone video services. All the pages will need to be in the similar design style.
The video's are targeted at consumers that want to sell there home and would like to have a cool drone video of photos of their home.

How does the website look:
- has a navbar on top
- A cool looking banner of an areal drone.
- A Big header: with company name: SkyNestClips
- A smaller subheader: We film your home to increase your chances of sale
- Then a section with a Big header: How does it work
- In this section a place for a vimeo explainitory video
- Then a similar navbar styled bar with a phone number and a email address
- Then a section where the videos porfolio is displayed in a cool way
- Inside this sectiona header: Our work

- A section with header: Why us?
- 4 symbols here with a subheader and some lorum ipsum text underneath (see wireframe images)

- Under that a: Contact us
- where you can put in name, email, phone, message box and a send button

- At the bottom a footer with phone number and a fake address for now.

Be creative. Use creative but serious color.
Use a serious font. Make it a sharp design. Sharp lines. Not to dark design and not to light design.

The wireframes are the same kind of images.
PLEASE PUT IN DESIGNS OF ALL THE PAGES

Good luck

Target Market(s)

People that want to sell home and want to make a cool drone video or photos of their home.

Industry/Entity Type

Business

Contact Information for Business Card

Lucas Verbeek
lucas@skynestclips.example
+31647203519

Logo Text

SkyNestClips

Number of Pages Required

1 page

Font styles to use
Sans Serif

Requirements
Must have
• All the sections as explained in the instructions.
• The nav bar should have an about us, services, portfolio and a contact us buttons.
• See instruction for details.
• Must include designs of the front page, contact us, our services, portfolio and contact us.
• If you do add some designs for the "about us", "services", "prices", "portfolio" and "contact us" pages, you make a way better chance of winning the competition.
Nice to have
• designs for the other pages as described at the Must haves. You make a better chance of winning if you include them. Look at the wireframes to see the mockups for those pages. think creative about what kind of sections and design should be included in those pages.
Should not have
• bad designs.

```html
<!DOCTYPE html>
<html lang="en">
<head>
<meta charset="utf-8">
<title>SkyNestClips – Home</title>
<link href="https://fonts.googleapis.com/css2?family=Poppins:wght@300;400;500;600;700&display=swap" rel="stylesheet">
<style>
:root{
  --accent:#1ba4e2;
  --accent-deep:#0b80c2;
  --teal:#1aa7b0;
  --ink:#151515;
  --text:#444;
  --bar:#2a2a2a;
  --footer:#3b3b3b;
  --footer-base:#1f1f1f;
  --star:#f3c64a;
  --white:#fff;
}
*{box-sizing:border-box;margin:0;padding:0}
html,body{width:1200px;height:3550px;overflow:hidden}
body{position:relative;font-family:'Poppins',sans-serif;color:var(--text);background:var(--white)}
.abs{position:absolute}

/* hero */
.hero{left:0;top:0;width:1200px;height:727px;background:radial-gradient(ellipse at 55% 35%,#6d6e6c 0%,#3c3d3b 45%,#1f201f 100%)}
.nav{left:0;top:0;width:1200px;height:95px;background:rgba(90,90,90,.55)}
.brand{left:48px;top:28px;font-size:30px;font-weight:600;color:var(--white);letter-spacing:.5px}
.nav-links{right:57px;top:34px;display:flex;gap:30px;list-style:none}
.nav-links li{font-size:19px;font-weight:500;color:var(--white);text-transform:uppercase}
.nav-links li.active{color:var(--accent);border-bottom:2px solid var(--accent);padding-bottom:4px}
.hero-title{left:0;top:300px;width:1200px;text-align:center;font-size:60px;font-weight:600;color:var(--white)}
.hero-sub{left:0;top:400px;width:1200px;text-align:center;font-size:25px;font-weight:300;color:var(--white);line-height:1.45}
.hero-btn{left:511px;top:511px;width:183px;height:57px;border:2px solid var(--white);color:var(--white);font-size:20px;font-weight:500;display:flex;align-items:center;justify-content:center;overflow:hidden}
.hero-btn::before{content:"";position:absolute;left:-2px;top:-2px;border-top:24px solid var(--accent);border-right:46px solid transparent}

/* section titles */
.section-title{left:0;width:1200px;text-align:center;font-size:40px;font-weight:600;color:var(--ink)}
.section-title span{color:var(--accent)}
.section-title::after{content:"";display:block;width:150px;height:2px;background:#8a8a8a;margin:8px auto 0}

/* how it works */
.how-text{left:57px;top:893px;width:490px;font-size:13.5px;line-height:1.65;color:#555}
.how-text p{margin-bottom:16px}
.video{left:632px;top:888px;width:464px;height:253px;background:radial-gradient(ellipse at 45% 50%,#6aa7ad 0%,#2d6a75 50%,#123a45 100%)}

/* contact bar */
.contact-bar{left:0;top:1238px;width:1200px;height:92px;background:var(--bar);color:var(--white);font-size:19px;letter-spacing:2px}
.contact-bar .item{top:32px;display:flex;align-items:center;gap:14px}

/* portfolio */
.card{top:1500px;width:253px;height:318px;background:var(--white);box-shadow:0 2px 6px rgba(0,0,0,.15);overflow:hidden}
.card-media{width:100%;height:252px;background:linear-gradient(180deg,#3a4a3a 0%,#5c6b55 45%,#a9b0a0 100%)}
.card-label{height:66px;background:var(--teal);color:var(--white);font-size:16px;display:flex;align-items:center;gap:8px;padding-left:22px}
.card-meta{top:1826px;width:253px;display:flex;justify-content:space-between;align-items:center;padding:0 10px}
.stars{color:var(--star);font-size:22px;letter-spacing:1px}
.actions{display:flex;gap:6px}
.actions span{width:24px;height:24px;border:2px solid var(--teal);border-radius:50%}
.arrow{top:1615px;width:26px;height:46px;background:var(--white);display:flex;align-items:center;justify-content:center;box-shadow:0 1px 3px rgba(0,0,0,.3)}

/* why us */
.why{left:0;top:2050px;width:1200px;height:727px;background:linear-gradient(180deg,#3d3a36 0%,#5a4a3c 55%,#7a5a3c 80%,#4a3a2e 100%)}
.why-side{left:0;top:2050px;width:331px;height:727px;background:#0c0c0c}
.diamond-label{width:200px;left:66px;text-align:center;color:var(--white);font-size:21px;font-weight:600}
.diamond-label small{display:block;font-size:15px;font-weight:400}
.why-head{left:421px;top:2185px;font-size:40px;font-weight:600;color:var(--white)}
.why-head::after{content:"";display:block;width:220px;height:2px;background:var(--white);margin-top:4px}
.why-text{left:431px;top:2278px;width:642px;font-size:14.5px;line-height:24px;color:#f0f0f0;text-align:justify}
.why-text p{margin-bottom:18px}
.why-more{left:431px;top:2572px;font-size:18px;color:var(--accent)}

/* contact form */
.field{border:1.5px solid #777;background:var(--white);font-size:13px;color:#555;padding:6px 22px}
.submit{left:497px;top:3212px;width:194px;height:44px;background:var(--accent-deep);color:var(--white);font-size:18px;font-weight:500;letter-spacing:1.5px;display:flex;align-items:center;justify-content:center}

/* footer */
.footer{left:0;top:3314px;width:1200px;height:170px;background:var(--footer)}
.footer-list{left:52px;top:3343px;list-style:none;color:var(--white);font-size:18px;letter-spacing:1px}
.footer-list li{display:flex;align-items:center;gap:18px;height:40px}
.social{right:50px;top:3376px;display:flex;gap:18px}
.social span{width:54px;height:54px;border-radius:50%;background:var(--white)}
.footer-base{left:0;top:3484px;width:1200px;height:66px;background:var(--footer-base);display:flex;align-items:center;justify-content:center;gap:14px;color:var(--white);font-size:15px}
.footer-base b{color:var(--accent);font-weight:600;font-size:20px}
</style>
</head>
<body>

<!-- Hero -->
<div class="abs hero" role="img" aria-label="Photo of a person holding up a camera drone against the sky"></div>
<header class="abs nav">
  <div class="abs brand">SkyNestClips</div>
  <ul class="abs nav-links">
    <li class="active">Home</li><li>Services</li><li>About Us</li><li>Portfolio</li><li>&nbsp;Contact Us</li>
  </ul>
</header>
<h1 class="abs hero-title">SkyNestClips</h1>
<p class="abs hero-sub">We Film Your Homes To Increase your<br>Chances Of Sale</p>
<div class="abs hero-btn">Read More</div>

<!-- How it works -->
<h2 class="abs section-title" style="top:755px">How Does <span>it Work?</span></h2>
<div class="abs how-text">
  <p>Lorem Ipsum is simply dummy text of the printing and typesetting industry. Lorem Ipsum has been the industry's standard dummy text ever since the 1500s, when an unknown printer took a galley of type and scrambled it to make a type specimen book</p>
  <p>It has survived not only five centuries, but also the leap into electronic typesetting, remaining essentially unchanged.</p>
  <p>It was popularised in the 1960s with the release of Glyphset sheets containing Lorem Ipsum passages, and more recently with desktop publishing software like Pressline Layout including versions of Lorem Ipsum.</p>
</div>
<div class="abs video" role="img" aria-label="Explainer video still of an ocean wave seen from above"></div>
<svg class="abs" style="left:632px;top:888px" width="464" height="253" viewBox="0 0 464 253">
  <circle cx="232" cy="126" r="11" fill="#1ba4e2" stroke="#fff" stroke-width="2"/>
  <path d="M229 120 L237 126 L229 132Z" fill="#fff"/>
  <rect x="0" y="234" width="464" height="19" fill="rgba(0,0,0,.55)"/>
  <rect x="30" y="242" width="360" height="3" fill="#777"/>
  <rect x="30" y="242" width="40" height="3" fill="#fff"/>
  <path d="M10 238 L18 243.5 L10 249Z" fill="#fff"/>
</svg>

<!-- Contact bar -->
<div class="abs contact-bar">
  <div class="abs item" style="left:260px">
    <svg width="24" height="24" viewBox="0 0 24 24" fill="none" stroke="#fff" stroke-width="1.6"><path d="M5 3h4l2 5-2.5 1.5a11 11 0 0 0 6 6L16 13l5 2v4a2 2 0 0 1-2 2A17 17 0 0 1 3 5a2 2 0 0 1 2-2z"/></svg>
    +31647203519
  </div>
  <div class="abs item" style="left:670px">
    <svg width="26" height="20" viewBox="0 0 26 20" fill="none" stroke="#fff" stroke-width="1.6"><rect x="1" y="1" width="24" height="18"/><path d="M1 1l12 10L25 1"/></svg>
    lucas@skynestclips.example
  </div>
</div>

<!-- Portfolio -->
<h2 class="abs section-title" style="top:1382px">Our <span>Work?</span></h2>
<div class="abs card" style="left:47px"><div class="card-media" role="img" aria-label="Portfolio still of a white drone hovering over trees"></div><div class="card-label"><svg width="12" height="16" viewBox="0 0 12 16"><path d="M6 0a6 6 0 0 1 6 6c0 4-6 10-6 10S0 10 0 6a6 6 0 0 1 6-6z" fill="#fff"/><circle cx="6" cy="6" r="2" fill="#1aa7b0"/></svg>Lorem Ipsum is simply</div></div>
<div class="abs card" style="left:331px"><div class="card-media" role="img" aria-label="Portfolio still of a white drone hovering over trees"></div><div class="card-label"><svg width="12" height="16" viewBox="0 0 12 16"><path d="M6 0a6 6 0 0 1 6 6c0 4-6 10-6 10S0 10 0 6a6 6 0 0 1 6-6z" fill="#fff"/><circle cx="6" cy="6" r="2" fill="#1aa7b0"/></svg>Lorem Ipsum is simply</div></div>
<div class="abs card" style="left:615px"><div class="card-media" role="img" aria-label="Portfolio still of a white drone hovering over trees"></div><div class="card-label"><svg width="12" height="16" viewBox="0 0 12 16"><path d="M6 0a6 6 0 0 1 6 6c0 4-6 10-6 10S0 10 0 6a6 6 0 0 1 6-6z" fill="#fff"/><circle cx="6" cy="6" r="2" fill="#1aa7b0"/></svg>Lorem Ipsum is simply</div></div>
<div class="abs card" style="left:899px"><div class="card-media" role="img" aria-label="Portfolio still of trees at dusk"></div><div class="card-label"><svg width="12" height="16" viewBox="0 0 12 16"><path d="M6 0a6 6 0 0 1 6 6c0 4-6 10-6 10S0 10 0 6a6 6 0 0 1 6-6z" fill="#fff"/><circle cx="6" cy="6" r="2" fill="#1aa7b0"/></svg>Lorem Ipsum is simply</div></div>
<div class="abs card-meta" style="left:47px"><span class="stars">★★★★☆</span><span class="actions"><span></span><span></span><span></span></span></div>
<div class="abs card-meta" style="left:331px"><span class="stars">★★★★☆</span><span class="actions"><span></span><span></span><span></span></span></div>
<div class="abs card-meta" style="left:615px"><span class="stars">★★★★☆</span><span class="actions"><span></span><span></span><span></span></span></div>
<div class="abs card-meta" style="left:899px"><span class="stars">★★★★☆</span></div>
<div class="abs arrow" style="left:36px"><svg width="12" height="20" viewBox="0 0 12 20"><path d="M10 2L2 10l8 8" stroke="#111" stroke-width="2.5" fill="none"/></svg></div>
<div class="abs arrow" style="left:1128px"><svg width="12" height="20" viewBox="0 0 12 20"><path d="M2 2l8 8-8 8" stroke="#111" stroke-width="2.5" fill="none"/></svg></div>

<!-- Why us -->
<h2 class="abs section-title" style="top:1920px">Why <span>Us?</span></h2>
<div class="abs why" role="img" aria-label="Dusk photo of a drone flying over a landscape at sunset"></div>
<div class="abs why-side"></div>
<svg class="abs" style="left:0;top:2050px" width="331" height="727" viewBox="0 0 331 727">
  <g stroke="#1ba4e2" stroke-width="2" fill="none">
    <path d="M166 28 L261 123 L166 218 L71 123Z" fill="#0b80c2" stroke="none"/>
    <path d="M166 186 L261 281 L166 376 L71 281Z"/>
    <path d="M166 338 L261 433 L166 528 L71 433Z"/>
    <path d="M166 504 L261 599 L166 694 L71 599Z"/>
  </g>
</svg>
<div class="abs diamond-label" style="top:2157px">Cheap</div>
<div class="abs diamond-label" style="top:2316px">Flexible</div>
<div class="abs diamond-label" style="top:2468px">Quality</div>
<div class="abs diamond-label" style="top:2620px">Increase<small>Sale</small></div>
<h3 class="abs why-head">Cheap:</h3>
<div class="abs why-text">
  <p>Lorem Ipsum is simply dummy text of the printing and typesetting industry. Lorem Ipsum has been the industry's standard dummy text ever since the 1500s, when an unknown printer took a galley of type and scrambled it to make a type specimen book. It has survived not only five centuries, but also the leap into electronic typesetting, remaining essentially unchanged. It was popularised in the 1960s with the release of Glyphset sheets containing Lorem Ipsum passages, and more recently with desktop publishing software like Pressline Layout including versions of Lorem Ipsum.</p>
  <p>It has survived not only five centuries, but also the leap into electronic typesetting, remaining essentially unchanged. It was popularised in the 1960s with the release of Glyphset sheets containing Lorem Ipsum passages, and more recently with desktop publishing software like Pressline Layout including versions of Lorem Ipsum.</p>
</div>
<div class="abs why-more">Read More...</div>

<!-- Contact -->
<h2 class="abs section-title" style="top:2815px">Contact <span>Us</span></h2>
<div class="abs field" style="left:317px;top:2907px;width:268px;height:35px">Name</div>
<div class="abs field" style="left:604px;top:2907px;width:267px;height:35px">Email</div>
<div class="abs field" style="left:317px;top:2968px;width:554px;height:38px">Phone</div>
<div class="abs field" style="left:317px;top:3034px;width:554px;height:138px">Enter Message</div>
<div class="abs submit">Submit</div>

<!-- Footer -->
<footer class="abs footer"></footer>
<ul class="abs footer-list">
  <li><svg width="24" height="18" viewBox="0 0 26 20" fill="none" stroke="#fff" stroke-width="1.6"><rect x="1" y="1" width="24" height="18"/><path d="M1 1l12 10L25 1"/></svg>Lorem Ipsum is simple dummy text, address.</li>
  <li><svg width="22" height="22" viewBox="0 0 24 24" fill="none" stroke="#fff" stroke-width="1.6"><path d="M5 3h4l2 5-2.5 1.5a11 11 0 0 0 6 6L16 13l5 2v4a2 2 0 0 1-2 2A17 17 0 0 1 3 5a2 2 0 0 1 2-2z"/></svg>+31647203519</li>
  <li><svg width="24" height="18" viewBox="0 0 26 20" fill="none" stroke="#fff" stroke-width="1.6"><rect x="1" y="1" width="24" height="18"/><path d="M1 1l12 10L25 1"/></svg>lucas@skynestclips.example</li>
</ul>
<div class="abs social" aria-label="Social media links"><span></span><span></span><span></span><span></span></div>
<div class="abs footer-base"><b>SkyNestClips</b>Copyrights 2016 , All rights Reserved</div>

</body>
</html>
```